Beautify our company's one pager website

We need a website - currently we have only a nice light-switcher: https://brindlequay.example

We got the basic contents together (see the wireframes - also in SVG format -
attached here). Now we need you (!) to make it look appealing, create proper illustrations, provide a good theme picture and advice us on how to take good employee pictures.

In the wireframes, the picture and most illustrations are just placeholders (only the logos of "Our Open Source tools" are ours - see attached logos.svg). We request you to fill all placeholders with good illustrations and make the whole page look nicely.

Only one color is pre-defined (#11233f - the blue color we use for our logo when it is on white background). Feel free to give it nice colours based on your professional expertise and intuition. Feel also free to use the blue in a more creative way, than proposed in the wireframes.

We will do the coding ourselves, but we request you to submit a responsive design, with at least one version for mobiles, one for tablet size and one for full desktop resolution.

We think our people pictures should follow a design line. Please asses us on how we should take our colleagues' pictures (e.g. completely white background, or... blurry city background, or.... with a big box in the hand, etc... we are curious to see your suggestion).

In case of any doubts, please don't hesitate to contact us (brindlequay-website-design@brindlequay.example).

Target Market(s)

International cooperation agencies

Industry/Entity Type

Consulting

Number of Pages Required

Font styles to use
Other font styles liked:
• Lato

Colors

Designer to choose colors to be used in the design.

Requirements
Must have
• Responsive design in mind (one pager, for three different resolutions: mobile, tablet, desktop)
• Illustrations and (maybe) a photo - must be royalty-free and open for any use in the future.
Nice to have
• SVG formated design
• Suggestions on the peoples' photos

```html
<!DOCTYPE html>
<html lang="en">
<head>
<meta charset="utf-8">
<title>Brindle Quay — Agile Consultancies</title>
<link rel="stylesheet" href="https://fonts.googleapis.com/css2?family=Poppins:wght@400;500;600&family=Lato:wght@400;700&display=swap">
<style>
:root{
  --navy:#11233f;
  --navy-deep:#0d1a33;
  --navy-mid:#1d3a6e;
  --royal:#24468a;
  --sky:#0ea5e9;
  --ink:#333a44;
  --muted:#6b7280;
  --light:#f3f3f3;
  --band:#e9e9ea;
  --white:#ffffff;
  --footer:#1e1f24;
}
*{box-sizing:border-box;margin:0;padding:0}
html,body{width:1200px;height:3571px;overflow:hidden}
body{position:relative;background:var(--white);font-family:"Lato",sans-serif;color:var(--ink)}
.abs{position:absolute}
h1,h2,h3,.brand,.nav a{font-family:"Poppins",sans-serif}
.btn{display:inline-block;border:1.5px solid currentColor;border-radius:24px;font-size:11px;font-weight:700;text-transform:uppercase;padding:0 22px;height:40px;line-height:37px;font-family:"Poppins",sans-serif}

/* hero */
.hero{left:0;top:0;width:1200px;height:507px;background:radial-gradient(ellipse at 30% 40%,#1f3466 0%,var(--navy-deep) 70%)}
.navbar{left:112px;top:33px;width:976px;height:62px;background:var(--navy-mid);display:flex;align-items:center;padding:0 18px}
.brand{color:var(--white);font-weight:600;font-size:28px;letter-spacing:1px}
.nav{margin-left:auto;display:flex;gap:68px}
.nav a{color:var(--white);text-decoration:none;font-size:13px;font-weight:500}
.hero-title{left:112px;top:186px;color:var(--white);font-size:40px;font-weight:600;letter-spacing:.5px;line-height:50px}
.hero-sub{left:112px;top:236px;color:var(--white);font-size:23px;font-weight:500;line-height:32px}
.hero-text{left:112px;top:280px;width:560px;color:#d8deea;font-size:12px;line-height:20px}
.hero-btn{left:112px;top:370px;color:var(--white)}
.laptop{left:614px;top:148px;width:472px;height:295px}

/* about */
.about-art{left:0;top:507px;width:369px;height:426px}
.about-title{left:338px;top:590px;color:var(--navy-mid);font-size:36px;font-weight:500;line-height:44px}
.about-text{left:338px;top:652px;width:380px;font-size:12px;line-height:21px;color:var(--muted)}
.about-btn{left:338px;top:821px;color:var(--navy)}
.about-photo{left:745px;top:598px;width:345px;height:245px;border:6px solid var(--white);box-shadow:0 4px 16px rgba(0,0,0,.18);background:linear-gradient(135deg,#cfd8e2,#e9edf1 55%,#b9a48c)}

/* agile band */
.agile{left:0;top:933px;width:1200px;height:193px;background:var(--band)}
.agile-title{left:0;top:963px;width:1200px;text-align:center;color:var(--navy-mid);font-size:38px;font-weight:500;line-height:48px}
.agile-text{left:190px;top:1034px;width:820px;text-align:center;font-size:13px;line-height:23px;color:var(--ink)}
.agile-corner{left:1015px;top:933px;width:185px;height:193px}

/* services */
.service{top:1160px;width:330px;text-align:center}
.service .icon{width:150px;height:120px;margin:0 auto;border-radius:6px}
.service h3{margin-top:20px;font-size:16px;font-weight:500;color:var(--navy-mid)}
.service p{margin:10px auto 0;width:300px;font-size:12px;line-height:20px;color:var(--muted)}
.service .btn{margin-top:22px;color:var(--navy);height:36px;line-height:33px;font-size:10px}

/* tools */
.tools{left:0;top:1505px;width:1200px;height:388px;background:linear-gradient(135deg,#1b3775,var(--navy-mid) 60%,#14285a)}
.tools-title{left:0;top:1575px;width:1200px;text-align:center;color:var(--white);font-size:36px;font-weight:500;line-height:44px}
.tool{top:1667px;width:488px;height:285px;text-align:center;padding:28px 36px}
.tool.primary{left:112px;background:var(--sky);color:var(--white)}
.tool.secondary{left:600px;background:var(--white);color:var(--muted);box-shadow:0 8px 14px rgba(0,0,0,.12)}
.tool h3{font-size:17px;font-weight:500;letter-spacing:1px;margin-top:8px}
.tool p{font-size:12px;line-height:20px;margin-top:14px}
.tool a{display:block;margin-top:14px;font-size:13px;color:inherit}
.tool.secondary h3,.tool.secondary a{color:var(--ink)}
.team-bg{left:0;top:1893px;width:1200px;height:1197px;background:var(--light)}

/* team */
.team-title{left:0;top:2010px;width:1200px;text-align:center;color:var(--navy-mid);font-size:36px;font-weight:500;line-height:44px}
.team-sub{left:0;top:2063px;width:1200px;text-align:center;font-size:13px;color:var(--muted)}
.member{width:300px;text-align:center}
.member .photo{width:186px;height:186px;border-radius:50%;margin:0 auto 16px;background:linear-gradient(160deg,#e3cdb8,#b98f72 55%,#8fa3b8)}
.member .photo.alt{background:linear-gradient(160deg,#ecd3b4,#d9a55a 50%,#3b4e6b)}
.member .photo.red{background:linear-gradient(160deg,#f1e3d6,#d9b49a 45%,#d2312d)}
.member h3{font-size:16px;font-weight:500;color:var(--navy)}
.member span{display:block;font-size:12px;color:var(--muted);margin-top:4px}
.member-card{left:452px;top:2429px;width:293px;height:300px;background:var(--white);box-shadow:0 4px 18px rgba(0,0,0,.12)}

/* footer */
.footer-left{left:0;top:3090px;width:631px;height:355px;background:var(--footer)}
.map{left:631px;top:3090px;width:569px;height:355px;background:linear-gradient(135deg,#e4e6e3,#d3d8d2 50%,#e8e2d2)}
.footer-brand{left:226px;top:3183px;font-size:26px;color:var(--white)}
.contact-line{left:226px;color:var(--white);font-size:13px;display:flex;gap:16px;align-items:flex-start}
.contact-line svg{flex:none}
.address{line-height:19px}
.address small{font-size:11px}
.extra-line{left:258px;top:3367px;color:var(--white);font-size:11px;line-height:26px}
.extra-line u{font-size:13px;font-weight:700}
.contact-box{left:521px;top:3131px;width:281px;height:279px;background:#2b2c30;padding:14px 18px}
.contact-box h3{color:var(--white);font-size:19px;font-weight:500}
.field{background:var(--white);height:42px;margin-top:12px;font-size:11px;color:#999;padding:10px 10px}
.field.first{margin-top:16px}
.field.tall{height:56px}
.send{margin-top:12px;width:90px;height:36px;background:var(--navy-mid);color:var(--white);font-size:11px;font-weight:700;text-align:center;line-height:36px;font-family:"Poppins",sans-serif}
.bottom{left:0;top:3445px;width:1200px;height:126px;background:var(--navy)}
.bottom-nav{left:0;top:3466px;width:1200px;display:flex;justify-content:center;gap:80px}
.bottom-nav a{color:var(--white);font-size:12px;text-decoration:none;font-family:"Poppins",sans-serif}
.social{left:0;top:3504px;width:1200px;display:flex;justify-content:center;gap:22px}
.social span{width:14px;height:14px;border-radius:50%;background:var(--white)}
.copy{left:0;top:3543px;width:1200px;text-align:center;color:#c8cfdc;font-size:11px}
</style>
</head>
<body>

<section class="hero abs" aria-label="Hero"></section>
<header class="navbar abs">
  <span class="brand">BRINDLE QUAY</span>
  <nav class="nav"><a href="#about">ABOUT</a><a href="#services">SERVICES</a><a href="#tools">TOOLS</a><a href="#team">TEAM</a><a href="#contact">CONTACT</a></nav>
</header>
<h1 class="abs hero-title">AGILE CONSULTANCIES</h1>
<h2 class="abs hero-sub">For International Development</h2>
<p class="abs hero-text">Brindle Quay provides institutions working in the international cooperation field (implementing agencies, local government and non-governmental institutions) with solutions (hardware, software and consultancy services) to better organize, manage and exchange their knowledge.</p>
<span class="abs btn hero-btn">Know more</span>
<svg class="abs laptop" viewBox="0 0 472 295" role="img" aria-label="Laptop showing an illustration of a city built from charts and documents">
  <rect x="30" y="0" width="412" height="270" rx="14" fill="#e7e9ee"/>
  <rect x="44" y="14" width="384" height="244" fill="#f6f1e4"/>
  <path d="M0 272h472l-20 16H20z" fill="#c9ccd3"/>
</svg>

<section class="about" id="about">
  <svg class="abs about-art" viewBox="0 0 369 426" role="img" aria-label="Photo of hands using a tablet, blue toned">
    <defs><linearGradient id="aboutGrad" x1="0" y1="0" x2="1" y2="1"><stop offset="0" stop-color="#3a5a9a"/><stop offset="1" stop-color="#162a55"/></linearGradient></defs>
    <polygon points="0,0 369,0 169,426 0,426" fill="url(#aboutGrad)"/>
  </svg>
  <h2 class="abs about-title">ABOUT US</h2>
  <p class="abs about-text">Lorem ipsum dolor sit amet, consectetuer adipiscing elit, sed diam nonummy nibh euismod tincidunt ut laoreet dolore magna aliquam erat volutpat. Ut wisi enim ad minim veniam, quis nostrud exerci tation ullamcorper suscipit lobortis nisl ut aliquip ex ea commodo consequat. Duis autem vel eum iriure dolor in hendrerit in vulputate velit esse molestie consequat, vel illum dolore eu feugiat nulla facilisis at vero eros.</p>
  <span class="abs btn about-btn">Read more</span>
  <div class="abs about-photo" role="img" aria-label="Photo of a smiling student holding folders"></div>
</section>

<section class="agile-section">
  <div class="abs agile"></div>
  <h2 class="abs agile-title">Agile</h2>
  <p class="abs agile-text">Efficient and flexible methodology for developing successful solutions with fun. Is is based on iterative, measurable and verifiable small steps, with integrative and empowering involvement of all actors.</p>
  <svg class="abs agile-corner" viewBox="0 0 185 193" aria-hidden="true"><polygon points="105,0 185,0 185,193 0,193" fill="var(--royal)"/></svg>
</section>

<section id="services">
  <div class="abs service" style="left:90px">
    <div class="icon" role="img" aria-label="Illustration of a monitor with coin charts" style="background:linear-gradient(#fbb040,#e94e1b)"></div>
    <h3>Technology For International Aid</h3>
    <p>Meaningful implementation and application of Digital Media, Software and Hardware with a sensibility for the world.</p>
    <span class="btn">Read more</span>
  </div>
  <div class="abs service" style="left:435px">
    <div class="icon" role="img" aria-label="Illustration of a monitor and phone with charts" style="background:linear-gradient(#2b3a55,#5fb8e6)"></div>
    <h3>Organizational Development</h3>
    <p>Agile and data-driven approach to accompany organizations into change processes, approach to accompany organizations.</p>
    <span class="btn">Read more</span>
  </div>
  <div class="abs service" style="left:780px">
    <div class="icon" role="img" aria-label="Illustration of a dashboard with clock and charts" style="background:linear-gradient(#3b82c4,#e74c3c)"></div>
    <h3>Data and Knowledge Management</h3>
    <p>Needs assessment, organizational and requirement analysis for ICT-based support to knowledge processes in communities of practice.</p>
    <span class="btn">Read more</span>
  </div>
</section>

<section id="tools">
  <div class="abs tools"></div>
  <h2 class="abs tools-title">OUR OPEN SOURCE TOOLS</h2>
  <div class="abs team-bg"></div>
  <div class="abs tool primary">
    <svg width="56" height="50" viewBox="0 0 56 50" aria-hidden="true"><rect x="6" y="8" width="44" height="34" rx="4" fill="none" stroke="#fff" stroke-width="3"/></svg>
    <h3>Q-CRATE</h3>
    <p>Open Source web based document management system. This Software allows organizational groups to flexibly manage their knowledge through documents and data. The files can be structured and access can be managed for groups of people or for specific persons.</p>
    <a href="#">https://code.brindlequay.example/q-crate</a>
  </div>
  <div class="abs tool secondary">
    <svg width="56" height="50" viewBox="0 0 56 50" aria-hidden="true"><rect x="8" y="6" width="40" height="40" fill="none" stroke="#333" stroke-width="3"/></svg>
    <h3>Q-BRIDGE</h3>
    <p>Several decentralized Q-Crates can be connected over a Q-Bridge. This allows to manage distributed instances and create organizational partnerships for networks of providing access to information and enhance knowledge in the developing world.</p>
    <a href="#">https://code.brindlequay.example/q-bridge</a>
  </div>
</section>

<section class="team" id="team">
  <h2 class="abs team-title">OUR TEAM</h2>
  <p class="abs team-sub">We are cultural technologists</p>
  <div class="abs member-card"></div>

  <div class="abs member" style="left:105px;top:2145px"><div class="photo" role="img" aria-label="Portrait photo of a team member"></div><h3>Dr. Matteo Ravelli</h3><span>Chief Executive Officer</span></div>
  <div class="abs member" style="left:450px;top:2145px"><div class="photo alt" role="img" aria-label="Portrait photo of a team member"></div><h3>Irina Volkova</h3><span>Chief Operations Officer</span></div>
  <div class="abs member" style="left:793px;top:2145px"><div class="photo red" role="img" aria-label="Portrait photo of a team member"></div><h3>Jonas Perrin</h3><span>Digital Product manager</span></div>

  <div class="abs member" style="left:105px;top:2459px"><div class="photo" role="img" aria-label="Portrait photo of a team member"></div><h3>Dr. Matteo Ravelli</h3><span>Chief Executive Officer</span></div>
  <div class="abs member" style="left:450px;top:2459px"><div class="photo alt" role="img" aria-label="Portrait photo of a team member"></div><h3>Irina Volkova</h3><span>Chief Operations Officer</span></div>
  <div class="abs member" style="left:793px;top:2459px"><div class="photo red" role="img" aria-label="Portrait photo of a team member"></div><h3>Jonas Perrin</h3><span>Digital Product manager</span></div>

  <div class="abs member" style="left:105px;top:2783px"><div class="photo" role="img" aria-label="Portrait photo of a team member"></div><h3>Dr. Matteo Ravelli</h3><span>Chief Executive Officer</span></div>
  <div class="abs member" style="left:450px;top:2783px"><div class="photo alt" role="img" aria-label="Portrait photo of a team member"></div><h3>Irina Volkova</h3><span>Chief Operations Officer</span></div>
  <div class="abs member" style="left:793px;top:2783px"><div class="photo red" role="img" aria-label="Portrait photo of a team member"></div><h3>Jonas Perrin</h3><span>Digital Product manager</span></div>
</section>

<footer id="contact">
  <div class="abs footer-left"></div>
  <div class="abs map" role="img" aria-label="Street map of the office location in Berlin"></div>
  <div class="abs brand footer-brand">BRINDLE QUAY</div>
  <div class="abs contact-line" style="top:3239px">
    <svg width="16" height="16" viewBox="0 0 24 24" aria-hidden="true"><path d="M6.6 10.8a15 15 0 006.6 6.6l2.2-2.2a1 1 0 011-.25 11 11 0 003.6.6 1 1 0 011 1V20a1 1 0 01-1 1A17 17 0 013 4a1 1 0 011-1h3.5a1 1 0 011 1 11 11 0 00.6 3.6 1 1 0 01-.25 1z" fill="#fff"/></svg>
    <span>(+12) 555 010 200</span>
  </div>
  <div class="abs contact-line" style="top:3272px">
    <svg width="16" height="14" viewBox="0 0 24 20" aria-hidden="true"><path d="M2 2h20v16H2z" fill="#fff"/><path d="M2 2l10 8 10-8" fill="none" stroke="#1e1f24" stroke-width="2"/></svg>
    <span style="font-size:11px">hello@brindlequay.example</span>
  </div>
  <div class="abs contact-line" style="top:3302px">
    <svg width="16" height="20" viewBox="0 0 24 30" aria-hidden="true"><path d="M12 0a10 10 0 00-10 10c0 8 10 20 10 20s10-12 10-20A10 10 0 0012 0z" fill="#fff"/><circle cx="12" cy="10" r="4" fill="#1e1f24"/></svg>
    <div class="address"><strong>Brindle Quay UG</strong><br><small>Lindenhof Str. 14, 10115 Berlin,<br>Germany</small></div>
  </div>
  <div class="abs extra-line">To be defined street Northgate, Valmora<br><u>Impressum</u></div>

  <form class="abs contact-box">
    <h3>CONTACT US</h3>
    <div class="field first">Name</div>
    <div class="field">Email</div>
    <div class="field tall">Message</div>
    <div class="send">SEND</div>
  </form>

  <div class="abs bottom"></div>
  <nav class="abs bottom-nav"><a href="#about">ABOUT</a><a href="#services">SERVICES</a><a href="#tools">TOOLS</a><a href="#team">TEAM</a><a href="#contact">CONTACT</a></nav>
  <div class="abs social" aria-label="Social links"><span></span><span></span><span></span><span></span></div>
  <p class="abs copy">Copyrights 2017 © All Rights Reserved</p>
</footer>

</body>
</html>
```